Superfoods Nutrition for Elderly

We need a thematic packaging design that fits our elderly nutrition products, that is based on our "3 Ws ethos" - eating Wisely, Widely & Wholly.

Wisely - selected superfoods and ingredients - NZ and other sources
Widely - based on the "rainbow diet" philosophy
Wholly - all natural, (no artificial flavours, colors etc). Formulated as complete meals (NOT supplementation)

Mediums:
- 400-450gram re-sealable doy packs
- 400-450gram re-sealable tin cans

Look n Feel:
Tamarewa - https://tamarewagoodness.example
Puke Nui - https://www.pukenui.example/
Harbour ledge - https://grainfieldpantry.example/collections/cereals

The name of our products may/may not be “vital mahi”. Our on-going research tells us that for the Asian market, an icon or character to personify our product may be a sound strategy. This is only for the designer to take note off.

Deliverables:
* 5 packaging designs in the range.
1x yellow + orange colored foods (star ingredient: “pure zing” – passion fruit powder)
1x red colored foods (star ingredient: (star ingredient: - Manuka honey )
1x blues/purple colored foods: (star ingredient: lorvane blackcurrant)
1 x green coloured foods (star ingredient: Green kiwi)
1 x brown/white (star ingredients: dunmore’s grass fed bone broth)

brand name, please use “VitalMahi” for now.

These will be the products:

Blue/purple: “Instant oatmeal porridge”
Ingredients: Rolled Baby Oats, Blueberries, Blackcurrant Powder, chia seeds, Blue Spirulina, Sheep’s Milk.
Star ingredient: Blackcurrant powder (support eyesight)

Brown/White: “Instant Brown Rice”
Ingredients: Organic Brown Rice, Grass fed bone broth powder, collagen peptide powder, black sesame seeds, onions and garlic powder, dried mushrooms, probiotics.
Star ingredient: Grass fed bone broth (support joint health)

Green: “Instant Smoothie”
Ingredients: Organic Green Kiwifruit, Kale powder, green apple powder, whey protein concentrate, probiotics, and sheep’s milk powder
Star ingredient: Organic green kiwi fruit(supports immunity)

Yellow/Orange “Instant Oatmeal”
Ingredients: Organic rolled baby oats, banana, organic passionfruit, apricot, dried mango, probiotics, cinnamon, sheep’s milk powder.
Star ingredient: Organic passionfruit(regulates blood glucose)

Red: “ instant amaranth cereal”
Ingredients: Organic amaranth, red apples, pomegranate, cranberries, Manuka honey powder, probiotics, sheep’s milk
Star ingredient: Manuka honey powder (anti-inflammatory)

Target Market(s)

Whose attention we are trying to grab?

Primary:
- 20 to 40 year olds buying these products for their parents/grand parents
- Health Nutrition conscious “golden agers”
Secondary
- Professional Caregivers to the elderly (homes, private hospitals etc)
- 40 year olds in the “prevention” mind set.

Font styles to use
Serif
Sans Serif

Colors

Designer to choose colors to be used in the design.

Requirements
Must have
• Mandatory:
• - clear visual que of the food color/s
• - "New Zealand" origin must come through strongly.
• - must have a blurp or feature of the star ingredient for each with mention of brand.
• e.g. for the blues+ purple, NZ blackcurrant powder for improved eyesight (cataract prevention).
• - icons for “heart health, “eyesight”, “mobility”, “gut-health”.
• - every other ingredient must be stated.
• The name of product may/may not be “vitalmahi”. Our on-going research tells us that for the Asian market, an icon or character to personify our product may be a sound strategy. This is only for the designer to take note off.
Nice to have
• Desirables:
• Ingredient origin story - e.g blackcurrant comes from Timaru etc.
• (refer to Pemberlys destination marketing…)

```html
<!DOCTYPE html>
<html lang="en">
<head>
<meta charset="utf-8">
<title>VitalMahi Instant Oatmeal – Pack Front</title>
<link rel="stylesheet" href="https://fonts.googleapis.com/css2?family=Raleway:ital,wght@0,300;0,400;0,500;0,700;0,800;1,400&display=swap">
<style>
  :root {
    --page-bg: #f4f4f2;
    --pack-white: #ffffff;
    --ink-dark: #3f3f3f;
    --ink-mid: #555555;
    --orange-bold: #f0a43a;
    --orange-light: #f3a94a;
    --band-yellow: #f6d83c;
    --rule-grey: #8a8a8a;
    --icon-gold: #e8c24a;
  }
  * { box-sizing: border-box; margin: 0; padding: 0; }
  html, body {
    width: 1200px; height: 758px; overflow: hidden;
    background: var(--page-bg);
    font-family: "Raleway", sans-serif;
  }
  .canvas { position: relative; width: 1200px; height: 758px; }
  .pack-front {
    position: absolute; left: 388px; top: 49px;
    width: 425px; height: 660px;
    background: var(--pack-white);
    box-shadow: 0 2px 14px rgba(0,0,0,0.08);
    overflow: hidden;
  }
  .brand-name {
    position: absolute; top: 54px; left: 0; width: 100%;
    text-align: center;
    font-weight: 800; font-size: 29px; letter-spacing: -0.5px;
    color: var(--ink-dark);
  }
  .hero-visual {
    position: absolute; left: 0; top: 96px; width: 425px; height: 316px;
    background:
      radial-gradient(ellipse 90px 80px at 72px 70px, #b9743f 0%, #c8864f 55%, rgba(200,134,79,0) 100%),
      radial-gradient(ellipse 150px 95px at 270px 140px, #f6d442 0%, #f1c534 55%, rgba(241,197,52,0) 100%),
      radial-gradient(ellipse 70px 60px at 130px 230px, #7a3b4a 0%, #8c4a52 60%, rgba(140,74,82,0) 100%),
      radial-gradient(ellipse 70px 45px at 105px 270px, #f0a03a 0%, #eda548 60%, rgba(237,165,72,0) 100%),
      radial-gradient(ellipse 75px 50px at 268px 268px, #cbb08a 0%, #d9c3a0 60%, rgba(217,195,160,0) 100%),
      var(--pack-white);
  }
  .product-type {
    position: absolute; top: 413px; left: 0; width: 100%;
    text-align: center;
    font-weight: 800; font-size: 24px; letter-spacing: 2px;
    color: var(--orange-bold);
  }
  .product-name {
    position: absolute; top: 437px; left: 0; width: 100%;
    text-align: center;
    font-weight: 300; font-size: 43px; letter-spacing: 2px;
    color: var(--orange-light);
  }
  .origin-band {
    position: absolute; top: 479px; left: 97px; width: 231px; height: 20px;
    background: var(--band-yellow);
    color: var(--pack-white);
    font-style: italic; font-weight: 400; font-size: 13px; letter-spacing: 1px;
    text-align: center; line-height: 20px;
  }
  .ingredients {
    position: absolute; top: 505px; left: 90px; width: 245px;
    text-align: center;
    font-size: 10px; line-height: 12px; color: var(--ink-mid);
  }
  .ingredients strong { font-weight: 700; color: var(--ink-dark); }
  .benefit-row {
    position: absolute; top: 573px; left: 97px; width: 231px; height: 37px;
    border-top: 1px solid var(--rule-grey);
    border-bottom: 1px solid var(--rule-grey);
    display: flex; justify-content: space-between; align-items: center;
  }
  .benefit {
    flex: 1; display: flex; flex-direction: column; align-items: center;
    border-left: 1px solid var(--rule-grey);
    height: 24px;
  }
  .benefit:first-child { border-left: 1px solid var(--rule-grey); }
  .benefit:last-child { border-right: 1px solid var(--rule-grey); }
  .benefit svg { width: 15px; height: 15px; }
  .benefit span { font-size: 4.5px; color: var(--ink-mid); margin-top: 2px; }
  .net-weight {
    position: absolute; top: 620px; left: 0; width: 100%;
    text-align: center; font-size: 15px; color: var(--ink-dark);
  }
</style>
</head>
<body>
<main class="canvas">
  <section class="pack-front">
    <div class="brand-name">VitalMahi</div>

    <div class="hero-visual" role="img" aria-label="Photo of a wooden spoon of cinnamon powder, a bunch of bananas, halved passionfruit, dried apricots and rolled oats"></div>

    <div class="product-type">INSTANT</div>
    <div class="product-name">OATMEAL</div>
    <div class="origin-band">NEW ZEALAND ORIGIN</div>

    <p class="ingredients">
      <strong>INGREDIENTS:</strong> Organic rolled baby oats, banana, organic passionfruit, apricot, dried mango, probiotics, cinnamon, sheep's milk powder.<br>
      <strong>STAR INGREDIENT:</strong> Organic passionfruit<br>
      (regulates blood glucose)
    </p>

    <div class="benefit-row">
      <div class="benefit">
        <svg viewBox="0 0 20 20" fill="none" stroke="var(--ink-mid)" stroke-width="1"><circle cx="10" cy="10" r="8.5"/><path d="M10 14 L6 10 A2.2 2.2 0 0 1 10 7 A2.2 2.2 0 0 1 14 10 Z"/></svg>
        <span>Heart Health</span>
      </div>
      <div class="benefit">
        <svg viewBox="0 0 20 20" fill="none" stroke="var(--ink-mid)" stroke-width="1"><circle cx="10" cy="10" r="8.5"/><path d="M4.5 10 Q10 5 15.5 10 Q10 15 4.5 10 Z"/><circle cx="10" cy="10" r="1.8"/></svg>
        <span>Eyesight</span>
      </div>
      <div class="benefit">
        <svg viewBox="0 0 20 20" fill="none" stroke="var(--ink-mid)" stroke-width="1"><circle cx="10" cy="10" r="8.5"/><circle cx="10" cy="5.5" r="1.3"/><path d="M10 7.5 V11.5 M10 11.5 L7.5 15 M10 11.5 L12.5 15 M7 9.5 H13"/></svg>
        <span>Mobility</span>
      </div>
      <div class="benefit">
        <svg viewBox="0 0 20 20" fill="none" stroke="var(--ink-mid)" stroke-width="1"><circle cx="10" cy="10" r="8.5"/><path d="M7 6 H13 V9 Q13 13 10 13 Q7 13 7 10 V6 M9 13 V15"/></svg>
        <span>Gut-health</span>
      </div>
    </div>

    <div class="net-weight">450G</div>
  </section>
</main>
</body>
</html>
```